need a graphic redesign of kestrowcare.com

Need a graphic redesign of kestrowcare.com. We need to make it more user friendly as well as SEO friendly. All information is there. We have lot of stock photos (done our own photoshoot).

We want this website to be redesigned from scratch. Please avoid using pre made templates. Recommend people who really understand design to approach this project.

Target population is Non resident Indians who live outside India but their families are still in India and need for health care.

Logos and pictures are on the website but we can provide raw images.

Target Market(s)

Industry/Entity Type

Healthcare

Number of Pages Required

5+ page

Font styles to use
Serif
Sans Serif

Requirements
Must have
• Good design, and use of minimal text. Design need to be responsive (we know it is a later process in coding- but mobile devices need to be kept in mind)
Nice to have
• We need a original design.
Should not have
• prebuilt or copied templates

```html
<!DOCTYPE html>
<html lang="en">
<head>
<meta charset="utf-8">
<title>Kestrow Care – Contact Us</title>
<link rel="stylesheet" href="https://fonts.googleapis.com/css2?family=Oswald:wght@300;400;500&family=Open+Sans:wght@400;600;700&display=swap">
<style>
:root{
  --green:#5f9b86;
  --green-dark:#3f6f5f;
  --green-deep:#2c4a40;
  --green-text:#3f8a70;
  --mint:#d3ebe0;
  --footer:#5c8f7d;
  --ink:#333;
  --white:#fff;
}
*{box-sizing:border-box;margin:0;padding:0}
html,body{width:826px;height:1200px;overflow:hidden;background:var(--white);font-family:"Open Sans",sans-serif;color:var(--ink)}
.page{position:relative;width:826px;height:1200px}
.abs{position:absolute}
.hero{left:0;top:0;width:826px;height:330px;background:linear-gradient(100deg,#e4eef2 0%,#b9d2d8 35%,#8fb7c0 60%,#a9c9cf 100%)}
.hero-title{left:490px;top:160px;font-family:"Oswald",sans-serif;font-weight:300;font-size:64px;color:var(--white);letter-spacing:1px}
.brand{left:0;top:0;width:124px;height:100px;background:var(--white);display:flex;flex-direction:column;align-items:center;justify-content:center;gap:6px}
.brand-dot{width:26px;height:26px;border-radius:50%;background:#e8873a}
.brand-name{font-family:"Oswald",sans-serif;font-size:15px;font-weight:400;color:var(--green-dark)}
.nav{left:124px;top:0;width:488px;height:48px;background:var(--green);display:flex;align-items:center;justify-content:space-around;padding:0 10px}
.nav a{font-family:"Oswald",sans-serif;font-size:12px;color:var(--white);text-decoration:none;letter-spacing:.5px}
.nav a.active{font-weight:500}
.login{left:612px;top:0;width:214px;height:115px;background:var(--mint);text-align:center;padding-top:6px}
.login small{display:block;font-size:8px;color:#577}
.pill{display:inline-block;border-radius:12px;background:var(--white);border:1px solid #9cc;font-family:"Oswald",sans-serif;font-size:13px;color:var(--green-dark);padding:3px 0;width:130px;margin:4px 0}
.intro{left:124px;top:348px;width:500px;font-family:"Oswald",sans-serif;font-weight:300;font-size:18px;line-height:26px;color:var(--green-text)}
.sidebar{left:612px;top:300px;width:214px;height:250px;background:var(--mint)}
.sidebar h3{position:absolute;top:8px;width:100%;text-align:center;font-family:"Oswald",sans-serif;font-weight:500;font-size:28px;color:var(--green-deep)}
.bubble{position:absolute;left:16px;top:50px}
.offline{position:absolute;left:10px;top:200px;width:194px;height:26px;border-radius:13px;background:var(--green-dark);color:var(--white);font-size:11px;display:flex;align-items:center;justify-content:center;gap:6px}
.offline b{font-weight:700}
.form-title{left:124px;top:432px;width:400px;text-align:center;font-family:"Oswald",sans-serif;font-weight:300;font-size:32px;color:var(--green-dark)}
.form{left:0;top:505px;width:560px}
.row{display:flex;align-items:center;height:42px}
.row label{width:242px;text-align:right;padding-right:12px;font-family:"Oswald",sans-serif;font-weight:400;font-size:12px;color:var(--ink)}
.field{width:244px;height:24px;border-radius:12px;border:1px solid #9a9a9a;border-top-color:#555;background:var(--white)}
.submit{left:248px;top:808px;width:137px;height:28px;border-radius:14px;background:var(--green-dark);color:var(--white);font-family:"Oswald",sans-serif;font-size:12px;display:flex;align-items:center;justify-content:center}
.footer{left:0;top:886px;width:826px;height:242px;background:var(--footer);color:var(--white)}
.footer h2{position:absolute;left:33px;top:26px;font-family:"Oswald",sans-serif;font-weight:300;font-size:30px}
.contact{position:absolute;left:33px;display:flex;align-items:center;gap:8px;font-size:12px}
.flag{position:absolute;width:44px;height:44px;border-radius:50%;background:#e9e3d6}
.office{position:absolute;top:40px;font-size:11px;line-height:17px}
.office h4{font-size:13px;font-weight:700;margin-bottom:4px}
.bar{left:0;top:1128px;width:826px;height:72px;background:var(--green-deep);display:flex;align-items:center;justify-content:center;gap:10px}
.bar span{width:30px;height:30px;border:1px solid var(--white)}
</style>
</head>
<body>
<div class="page">
  <div class="abs hero" role="img" aria-label="Team of smiling doctors and nurses in scrubs and white coats"></div>
  <div class="abs hero-title">CONTACT US</div>

  <div class="abs brand"><span class="brand-dot"></span><span class="brand-name">Kestrow Care</span></div>
  <nav class="abs nav">
    <a href="#">HOME</a><a href="#">ABOUT US</a><a href="#">SERVICES</a><a href="#">OUR NETWORK</a><a href="#">PARTNER WITH US</a><a href="#" class="active">CONTACT US</a>
  </nav>

  <div class="abs login">
    <small>Login to access your account</small>
    <div class="pill">MEMBER LOGIN</div>
    <small>Become a member to get all benefits</small>
    <div class="pill">SIGN UP</div>
  </div>

  <p class="abs intro">Please fill out the form below and we will get in touch with you as quickly as we can.</p>

  <aside class="abs sidebar">
    <h3>QUESTION?</h3>
    <svg class="bubble" width="182" height="140" viewBox="0 0 182 140">
      <path d="M8 6 H174 V100 H60 L30 132 L34 100 H8 Z" fill="#fff" stroke="#2c4a40" stroke-width="5" stroke-linejoin="round"/>
      <text x="91" y="66" text-anchor="middle" font-family="Oswald, sans-serif" font-weight="500" font-size="28" fill="#2c4a40">LIVE CHAT</text>
    </svg>
    <div class="offline"><b>OFFLINE</b> Leave message</div>
  </aside>

  <h2 class="abs form-title">GET IN TOUCH</h2>
  <form class="abs form">
    <div class="row"><label>Name</label><span class="field"></span></div>
    <div class="row"><label>Mobile Number</label><span class="field"></span></div>
    <div class="row"><label>Alternative Contact Number</label><span class="field"></span></div>
    <div class="row"><label>Email</label><span class="field"></span></div>
    <div class="row"><label>City</label><span class="field"></span></div>
    <div class="row"><label></label><span class="field"></span></div>
    <div class="row"><label></label><span class="field"></span></div>
  </form>
  <div class="abs submit">SUBMIT</div>

  <footer class="abs footer">
    <h2>Get in touch</h2>
    <div class="contact" style="top:92px">
      <svg width="16" height="16" viewBox="0 0 24 24"><circle cx="12" cy="12" r="12" fill="#fff"/><path d="M8 6l2 0 1 3-1.5 1a7 7 0 0 0 3.5 3.5l1-1.5 3 1v2a2 2 0 0 1-2 2A10 10 0 0 1 6 8a2 2 0 0 1 2-2z" fill="#5c8f7d"/></svg>
      +91 120 555 0148
    </div>
    <div class="contact" style="top:128px">
      <svg width="16" height="16" viewBox="0 0 24 24"><circle cx="12" cy="12" r="12" fill="#fff"/><rect x="6" y="8" width="12" height="8" fill="none" stroke="#5c8f7d" stroke-width="1.6"/><path d="M6 8l6 5 6-5" fill="none" stroke="#5c8f7d" stroke-width="1.6"/></svg>
      info@kestrowcare.com
    </div>
    <span class="flag" style="left:240px;top:38px"></span>
    <div class="office" style="left:302px">
      <h4>Registered Office</h4>
      Level 4, Orchid Plaza,<br>Sector 12 Road<br>Gurgaon 122002<br>Haryana, India
    </div>
    <div class="office" style="left:455px">
      <h4>Corporate Office:</h4>
      210 Linden Court,<br>Park Street Centre<br>New Delhi 110025<br>Landline No : 11 5550 4821<br>Fax No : 11 5550 4822
    </div>
    <span class="flag" style="left:620px;top:38px"></span>
    <div class="office" style="left:680px">
      <h4>Our US Office:</h4>
      4120 W Maple Road,<br>Suite 204<br>Peoria, AZ 85381<br>United States
    </div>
  </footer>
  <div class="abs bar">
    <span></span><span></span><span></span><span></span><span></span><span></span><span></span><span></span>
  </div>
</div>
</body>
</html>
```